Boilerplate Management Organization Chart

"Our Management Approach is a deliberate step-by-step process and supports our Technical Approach detailed in proposal submission. The Management Approach covers all the human capital aspects for executing a contract—from contract award through to sustainment and/or transition of the contract to another company. It includes how we organize, hire, staff, train, and account for our contract employees—as well as their complete personal life-cycle management within the company."

We need this management approach to depict an amazing management process that demonstrates best practices of the project management body of knowledge. We need this vector image to be applicable to any proposal without making references to any other proposals. Generic names but using strong business language.
Updates

Thanks for all designs submitted thus far. Some have stuck to the original type of chart. We would like to see a completely different way to show the same information. It has to be able to be recognized and deciphered very quickly by people who might not necessarily want to look at it. It must draw them in and make it incredibly easy to distinguish a management approach that looks fresh, infallible, and easily implemented.

Target Market(s)

Federal space, Government organizations looking for procedural efficiencies,

Industry/Entity Type

Management

Requirements
Must have
• Must not take up more than 1/3 to 1/2 of printable page and be clear.
Should not have
• Not too much color, but should stick to some color palette of some interest.

```html
<!DOCTYPE html>
<html lang="en">
<head>
<meta charset="utf-8">
<title>Management Approach Cycle</title>
<link rel="stylesheet" href="https://fonts.googleapis.com/css2?family=Montserrat:wght@600;700;800&display=swap">
<style>
  :root {
    --navy: #05055f;
    --green: #066004;
    --olive: #8fa000;
    --teal: #a7c4be;
    --rim: #d0d0d0;
    --ray: #7a7a7a;
    --label: #dedede;
    --page: #ffffff;
  }
  html, body {
    margin: 0;
    padding: 0;
    width: 1200px;
    height: 1200px;
    overflow: hidden;
    background: var(--page);
  }
  .cycle-chart {
    display: block;
    width: 1200px;
    height: 1200px;
    font-family: "Montserrat", sans-serif;
  }
  .rim { fill: var(--rim); }
  .field { fill: var(--teal); }
  .ray { stroke: var(--ray); stroke-width: 1.5; }
  .banner { fill: var(--navy); stroke: var(--rim); stroke-width: 6; }
  .banner-title {
    fill: var(--label);
    font-weight: 800;
    font-size: 90px;
  }
  .step-navy { fill: var(--navy); }
  .step-green { fill: var(--green); }
  .step-olive { fill: var(--olive); }
  .step-label {
    fill: var(--label);
    font-weight: 700;
    font-size: 32px;
    letter-spacing: 1px;
    text-anchor: middle;
    dominant-baseline: middle;
  }
  .step-label.large { font-size: 46px; }
  .step-number {
    fill: var(--label);
    font-weight: 800;
    font-size: 36px;
    text-anchor: middle;
    dominant-baseline: middle;
  }
</style>
</head>
<body>
<svg class="cycle-chart" viewBox="0 0 1500 1500" role="img" aria-label="Eight step management approach cycle framed by Management Approach and Program Evaluation">
  <defs>
    <path id="arc-top" d="M195.3,509.4 A612 612 0 0 1 1304.7,509.4"/>
    <path id="arc-bottom" d="M152.4,1113 A690 690 0 0 0 1347.6,1113"/>
    <polygon id="step-arrow" points="750,368 750,278 819.6,328.5"/>
  </defs>

  <g class="backdrop">
    <circle class="rim" cx="750" cy="768" r="662"/>
    <circle class="field" cx="750" cy="768" r="650"/>
  </g>

  <g class="rays">
    <line class="ray" x1="750" y1="768" x2="750" y2="130"/>
    <line class="ray" x1="750" y1="768" x2="750" y2="1420"/>
    <line class="ray" x1="750" y1="768" x2="100" y2="768"/>
    <line class="ray" x1="750" y1="768" x2="1400" y2="768"/>
    <line class="ray" x1="750" y1="768" x2="1199" y2="319"/>
    <line class="ray" x1="750" y1="768" x2="301" y2="319"/>
    <line class="ray" x1="750" y1="768" x2="1199" y2="1217"/>
    <line class="ray" x1="750" y1="768" x2="301" y2="1217"/>
  </g>

  <g class="steps">
    <path class="step-navy"  d="M825.2,233.2 A540 540 0 0 1 1131.8,386.2 L993.9,524.1 A345 345 0 0 0 798,426.4 Z"/>
    <path class="step-green" d="M1181.2,443 A540 540 0 0 1 1290,768 L1095,768 A345 345 0 0 0 1025.5,560.4 Z"/>
    <path class="step-olive" d="M1284.8,843.2 A540 540 0 0 1 1131.8,1149.8 L993.9,1011.9 A345 345 0 0 0 1091.6,816 Z"/>
    <path class="step-navy"  d="M1075,1199.2 A540 540 0 0 1 750,1308 L750,1113 A345 345 0 0 0 957.6,1043.5 Z"/>
    <path class="step-navy"  d="M674.8,1302.8 A540 540 0 0 1 368.2,1149.8 L506.1,1011.9 A345 345 0 0 0 702,1109.6 Z"/>
    <path class="step-olive" d="M318.8,1093 A540 540 0 0 1 210,768 L405,768 A345 345 0 0 0 474.5,975.6 Z"/>
    <path class="step-green" d="M215.2,692.8 A540 540 0 0 1 368.2,386.2 L506.1,524.1 A345 345 0 0 0 408.4,720 Z"/>
    <path class="step-navy"  d="M425,336.8 A540 540 0 0 1 750,228 L750,423 A345 345 0 0 0 542.4,492.5 Z"/>
  </g>

  <g class="step-arrows">
    <g transform="rotate(0 750 768)"><use href="#step-arrow" class="step-navy"/><text class="step-number" x="778" y="324" transform="rotate(4 778 324)">1</text></g>
    <g transform="rotate(45 750 768)"><use href="#step-arrow" class="step-green"/><text class="step-number" x="778" y="324" transform="rotate(4 778 324)">2</text></g>
    <g transform="rotate(90 750 768)"><use href="#step-arrow" class="step-olive"/><text class="step-number" x="778" y="324" transform="rotate(4 778 324)">3</text></g>
    <g transform="rotate(135 750 768)"><use href="#step-arrow" class="step-navy"/><text class="step-number" x="778" y="324" transform="rotate(4 778 324)">4</text></g>
    <g transform="rotate(180 750 768)"><use href="#step-arrow" class="step-navy"/><text class="step-number" x="778" y="324" transform="rotate(4 778 324)">5</text></g>
    <g transform="rotate(225 750 768)"><use href="#step-arrow" class="step-olive"/><text class="step-number" x="778" y="324" transform="rotate(4 778 324)">6</text></g>
    <g transform="rotate(270 750 768)"><use href="#step-arrow" class="step-green"/><text class="step-number" x="778" y="324" transform="rotate(4 778 324)">7</text></g>
    <g transform="rotate(315 750 768)"><use href="#step-arrow" class="step-navy"/><text class="step-number" x="778" y="324" transform="rotate(4 778 324)">8</text></g>
  </g>

  <g class="step-labels">
    <text class="step-label" x="948.6" y="369.8" transform="rotate(26.5 948.6 369.8)"><tspan x="948.6" dy="-20">Responsibility</tspan><tspan x="948.6" dy="40">Fixed</tspan></text>
    <text class="step-label" x="1172" y="626.8" transform="rotate(71.5 1172 626.8)"><tspan x="1172" dy="-20">Management</tspan><tspan x="1172" dy="40">&amp; Oversight</tspan></text>
    <text class="step-label" x="1148.2" y="966.6" transform="rotate(116.5 1148.2 966.6)" style="font-size:40px"><tspan x="1148.2" dy="-22">Manning</tspan><tspan x="1148.2" dy="44">the Team</tspan></text>
    <text class="step-label large" x="891.2" y="1190" transform="rotate(161.5 891.2 1190)">Training</text>
    <text class="step-label" x="551.4" y="1166.2" transform="rotate(206.5 551.4 1166.2)"><tspan x="551.4" dy="-20">Professional</tspan><tspan x="551.4" dy="40">Development</tspan></text>
    <text class="step-label" x="328" y="909.2" transform="rotate(251.5 328 909.2)" style="font-size:28px"><tspan x="328" dy="-20">Retention/</tspan><tspan x="328" dy="40">Quality of Life</tspan></text>
    <text class="step-label large" x="351.8" y="569.4" transform="rotate(296.5 351.8 569.4)">Benefits</text>
    <text class="step-label" x="608.8" y="346" transform="rotate(341.5 608.8 346)"><tspan x="608.8" dy="-20">Sustainment/</tspan><tspan x="608.8" dy="40">Transition</tspan></text>
  </g>

  <g class="banners">
    <path class="banner" d="M130.8,410.5 A715 715 0 0 1 1369.2,410.5 L1261,473 A590 590 0 0 0 239,473 Z"/>
    <text class="banner-title"><textPath href="#arc-top" startOffset="50%" text-anchor="middle" textLength="1190" lengthAdjust="spacingAndGlyphs">MANAGEMENT APPROACH</textPath></text>
    <path class="banner" d="M196.7,1216.1 A712 712 0 0 0 1303.3,1216.1 L1213.9,1143.7 A597 597 0 0 1 286.1,1143.7 Z"/>
    <text class="banner-title"><textPath href="#arc-bottom" startOffset="50%" text-anchor="middle" textLength="1110" lengthAdjust="spacingAndGlyphs">PROGRAM EVALUATION</textPath></text>
  </g>
</svg>
</body>
</html>
```